Maple Hollow Farm Business Card

Farm selling Nigerian Dwarf Goats, Bison, chickens, and miniature donkeys. Additionally we sell goats milk, goats milk soap and goat cheese, bison meat, bison heads, and bison skins, and chicken eggs.
Address 4125 Larkspur Road
Brookvale, KY 40999
Phone number 555-283-1947
Website: MapleHollowFarm@examplemail.com
I will upload my farm logo, cheese label, and soap label to give you ideas of my theme.
I want a really catchy card that people will remember.

```html
<!DOCTYPE html>
<html lang="en">
<head>
<meta charset="utf-8">
<title>Maple Hollow Farm Business Card</title>
<link rel="stylesheet" href="https://fonts.googleapis.com/css2?family=Federo&family=Jost:wght@400&family=Open+Sans:wght@400&display=swap">
<style>
  :root {
    --canvas: #ffffff;
    --label-red: #e8202a;
    --front-bg: #000000;
    --accent-orange: #f15a24;
    --accent-green: #2db34a;
    --ink: #1a1a1a;
    --frame: #333333;
    --badge-brown: #3a2f22;
  }
  * { margin: 0; padding: 0; box-sizing: border-box; }
  html, body {
    width: 1000px;
    height: 1200px;
    overflow: hidden;
    background: var(--canvas);
  }
  .sheet {
    position: relative;
    width: 1000px;
    height: 1200px;
  }
  .design-label {
    position: absolute;
    top: 22px;
    left: 0;
    width: 1000px;
    text-align: center;
    font-family: "Open Sans", sans-serif;
    font-weight: 400;
    font-size: 40px;
    line-height: 54px;
    color: var(--label-red);
  }
  .card-front {
    position: absolute;
    left: 45px;
    top: 88px;
    width: 911px;
    height: 522px;
    background: var(--front-bg);
  }
  .front-name {
    position: absolute;
    inset: 0;
    display: flex;
    align-items: center;
    justify-content: center;
    gap: 22px;
  }
  .front-name__mark {
    width: 34px;
    height: 34px;
    background: var(--accent-green);
  }
  .front-name__text {
    font-family: "Federo", sans-serif;
    font-size: 54px;
    letter-spacing: 3px;
    color: var(--accent-orange);
    text-transform: uppercase;
  }
  .card-back {
    position: absolute;
    left: 45px;
    top: 645px;
    width: 911px;
    height: 524px;
    background: var(--canvas);
    border: 2px solid var(--frame);
  }
  .back-brand {
    position: absolute;
    left: 95px;
    top: 214px;
    display: flex;
    align-items: center;
    gap: 14px;
  }
  .back-brand__mark {
    width: 86px;
    height: 80px;
    background: var(--badge-brown);
  }
  .back-brand__name {
    font-family: "Jost", sans-serif;
    font-size: 20px;
    color: var(--ink);
  }
  .contact {
    position: absolute;
    left: 90px;
    top: 306px;
    font-family: "Jost", sans-serif;
    font-size: 24px;
    line-height: 32.5px;
    color: var(--ink);
    font-style: normal;
    white-space: nowrap;
  }
  .deer-art {
    position: absolute;
    top: 336px;
  }
  .deer-art--orange { left: 432px; }
  .deer-art--green { left: 490px; }
</style>
</head>
<body>
<div class="sheet">
  <h1 class="design-label">Design-2</h1>

  <section class="card-front">
    <div class="front-name">
      <span class="front-name__mark"></span>
      <span class="front-name__text">Maple Hollow Farm</span>
    </div>
  </section>

  <section class="card-back">
    <div class="back-brand">
      <span class="back-brand__mark"></span>
      <span class="back-brand__name">Maple Hollow Farm</span>
    </div>

    <address class="contact">
      4125 Larkspur Road<br>
      Brookvale, KY 40999<br>
      Phone: 555-283-1947<br>
      Website: MapleHollowFarm@examplemail.com
    </address>

    <svg class="deer-art deer-art--orange" width="44" height="66" viewBox="0 0 44 66" role="img" aria-label="Orange line drawing of a buck's head with antlers">
      <rect x="0" y="0" width="44" height="66" rx="6" fill="var(--accent-orange)" opacity="0.85"/>
    </svg>
    <svg class="deer-art deer-art--green" width="40" height="66" viewBox="0 0 40 66" role="img" aria-label="Green line drawing of a buck's head with antlers">
      <rect x="0" y="0" width="40" height="66" rx="6" fill="var(--accent-green)" opacity="0.85"/>
    </svg>
  </section>
</div>
</body>
</html>
```